ParlaShift - Brighter relocation answers, Now!

Hello,
I'd like to update, re-vamp, and re-tool this current power point presentation with slightly more professional appearance as well as more accurately reflect the website -parlashift.com- color scheme and sleek design scheme. Please see attached.
We at ParlaShift pride ourselves on seeking to rework an archaic business into something progressive, cost effective, more reliable, and easily accessible in todays fast growing market that has only gotten more expensive, more costly and less indirect over the last couple years.

Target Market(s)

New updated and hassle free moving opportunities no matter how large or how small in a market that begs for a change

Industry/Entity Type

Logistics/Moving

Requirements
Must have
• The current color scheme from the -parlashift.com- website as well as the inclusion of the current data on the sample power point presentation provided but with updated graphics

```html
<!DOCTYPE html>
<html lang="en">
<head>
<meta charset="utf-8">
<title>ParlaShift – Credential Presentation</title>
<link href="https://fonts.googleapis.com/css2?family=Open+Sans:wght@300;400;600;700&display=swap" rel="stylesheet">
<style>
  :root{
    --page-bg:#e6e9ee;
    --slide-bg:#ffffff;
    --brand-blue:#1565d8;
    --navy:#0f2344;
    --deep-blue:#214b86;
    --muted:#4a5576;
    --body-text:#5b6270;
    --accent-yellow:#f5c342;
    --photo-top:#bfd6d0;
    --photo-mid:#a9b7b5;
    --photo-bottom:#d9b98f;
  }
  *{box-sizing:border-box;margin:0;padding:0}
  html,body{width:1081px;height:1200px;overflow:hidden}
  body{background:var(--page-bg);font-family:"Open Sans",Arial,sans-serif;position:relative}
  .slide{position:absolute;left:153px;width:790px;height:438px;background:var(--slide-bg);
    box-shadow:0 14px 26px rgba(120,135,160,.35)}
  .slide--cover{top:139px}
  .slide--about{top:622px}

  /* cover */
  .brand{position:absolute;left:0;right:0;top:120px;display:flex;justify-content:center;align-items:center;gap:10px}
  .brand__mark{width:22px;height:22px;background:var(--brand-blue)}
  .brand__name{font-size:28px;font-weight:700;color:var(--brand-blue);letter-spacing:.5px}
  .cover__title{position:absolute;left:0;right:0;top:182px;text-align:center;font-size:26px;font-weight:700;color:var(--navy)}
  .cover__subtitle{position:absolute;left:0;right:0;top:226px;text-align:center;font-size:14px;font-weight:300;color:var(--muted)}
  .cover__presenter{position:absolute;left:0;right:0;top:293px;text-align:center;font-size:16px;font-weight:700;color:var(--deep-blue)}
  .cover__date{position:absolute;left:37px;top:396px;font-size:11px;color:#3a3a2e}
  .cover__date span{color:var(--brand-blue)}
  .cover__site{position:absolute;right:37px;top:395px;font-size:11px;color:#3a3a2e;letter-spacing:.3px}

  /* about */
  .about__photo{position:absolute;left:83px;top:93px;width:210px;height:252px;
    background:linear-gradient(180deg,var(--photo-top) 0%,var(--photo-mid) 55%,var(--photo-bottom) 100%);
    box-shadow:0 8px 16px rgba(0,0,0,.18)}
  .about__rule{position:absolute;left:346px;top:92px;width:37px;height:2px;background:var(--accent-yellow)}
  .about__heading{position:absolute;left:345px;top:98px;font-size:27px;font-weight:700;color:#000}
  .about__body{position:absolute;left:347px;top:163px;width:360px;font-size:9.6px;line-height:17.5px;
    color:var(--body-text);letter-spacing:.3px}
  .about__body p+p{margin-top:17.5px}

  .footer-bar{position:absolute;left:0;right:0;top:414px;height:18px;background:var(--deep-blue)}
  .footer-bar__brand{position:absolute;left:8px;top:0;width:91px;height:18px;background:var(--slide-bg);
    display:flex;align-items:center;gap:5px;padding-left:4px}
  .footer-bar__brand-mark{width:9px;height:9px;background:var(--brand-blue)}
  .footer-bar__brand-name{font-size:12px;font-weight:700;color:var(--brand-blue)}
  .footer-bar__site{position:absolute;left:0;right:0;top:1px;text-align:center;font-size:11px;color:#fff;letter-spacing:.3px}
  .footer-bar__page{position:absolute;right:25px;top:1px;font-size:11px;color:#fff}
  .footer-bar__page i{display:inline-block;width:1px;height:12px;background:#fff;margin:0 6px;vertical-align:-2px}
</style>
</head>
<body>

<section class="slide slide--cover">
  <div class="brand"><span class="brand__mark"></span><span class="brand__name">ParlaShift</span></div>
  <h1 class="cover__title">Moving For The Next Generation</h1>
  <p class="cover__subtitle">Credential Subtitle Presentation</p>
  <p class="cover__presenter">Mr. Adrian Vell</p>
  <p class="cover__date">June <span>2023</span></p>
  <p class="cover__site">parlashift.com</p>
</section>

<section class="slide slide--about">
  <div class="about__photo" role="img" aria-label="Photo of a happy person stretching on the floor among moving boxes"></div>
  <div class="about__rule"></div>
  <h2 class="about__heading">About Us</h2>
  <div class="about__body">
    <p>ParlaShift is the next logical evolution in professional moving. Professional moving clients have battled soaring prices, acute capacity problems and deteriorating service levels.</p>
    <p>ParlaShift was founded by lifelong moving professionals who have developed the answer to better moving services. Poised as THE industry disruptor, we deliver faster, offer guaranteed prices and even offer no credit check financing options. We are a technology first organization using proprietary software to deliver moving's best service experience.</p>
  </div>
  <div class="footer-bar">
    <div class="footer-bar__brand"><span class="footer-bar__brand-mark"></span><span class="footer-bar__brand-name">ParlaShift</span></div>
    <span class="footer-bar__site">parlashift.com</span>
    <span class="footer-bar__page">page<i></i>2</span>
  </div>
</section>

</body>
</html>
```